"Harbor Constructors" is a residential building company and needs a new business card design and may re

We would like a redesign based on the existing logo, and would like to see a new font as well. We are bespoke home builders who build sustainable energy efficient homes.

Industry/Entity Type

Construction

Contact Information for Business Card

Business card size 40mm x 90mm

Colors

Designer to choose colors to be used in the design.

```html
<!DOCTYPE html>
<html lang="en">
<head>
<meta charset="utf-8">
<title>Harbor Constructors – Business Card</title>
<link rel="stylesheet" href="https://fonts.googleapis.com/css2?family=Roboto:wght@400;500;700&family=Roboto+Condensed:wght@700&display=swap">
<style>
  :root {
    --stage: #e9e6e1;
    --card-dark: #1d1d1d;
    --card-light: #f4f4f4;
    --lime: #b5d334;
    --ink: #111111;
    --white: #ffffff;
  }
  * { margin: 0; padding: 0; box-sizing: border-box; }
  html, body { width: 1200px; height: 960px; overflow: hidden; }
  body {
    background: var(--stage);
    font-family: "Roboto", Arial, sans-serif;
    position: relative;
  }
  .card {
    position: absolute;
    width: 600px;
    height: 343px;
    overflow: hidden;
    box-shadow: 0 4px 12px rgba(0,0,0,.25);
  }
  /* front */
  .card--front { left: 302px; top: 128px; background: var(--card-dark); }
  .front-panel { position: absolute; inset: 0; }
  .brand { position: absolute; display: flex; align-items: center; }
  .brand__square { display: block; background: var(--lime); }
  .brand__name { font-family: "Roboto", Arial, sans-serif; font-weight: 500; white-space: nowrap; }
  .card--front .brand { left: 26px; top: 122px; gap: 9px; }
  .card--front .brand__square { width: 22px; height: 22px; }
  .card--front .brand__name { font-size: 22px; color: var(--lime); }
  .holder-name {
    position: absolute; left: 51px; top: 190px;
    font-family: "Roboto Condensed", "Arial Narrow", sans-serif;
    font-weight: 700; font-size: 21px; color: var(--lime); letter-spacing: .2px;
  }
  .contact {
    position: absolute; right: 27px; top: 94px;
    text-align: right; color: var(--ink); font-size: 14px; line-height: 18px;
  }
  .contact__company { font-weight: 700; }
  .contact__gap { margin-top: 3px; }
  .contact__line { display: flex; justify-content: flex-end; align-items: center; gap: 8px; }
  .contact__icon { width: 12px; height: 12px; flex: none; }
  /* back */
  .card--back { left: 299px; top: 488px; background: var(--card-light); }
  .card--back .brand { left: 0; right: 0; top: 120px; justify-content: center; gap: 14px; }
  .card--back .brand__square { width: 36px; height: 36px; }
  .card--back .brand__name { font-size: 40px; color: var(--ink); }
  .web-band {
    position: absolute; left: 0; right: 0; top: 294px; height: 26px;
    background: var(--card-dark); color: var(--white);
    font-size: 14px; letter-spacing: 2.4px; text-align: center; line-height: 26px;
  }
</style>
</head>
<body>
  <section class="card card--front" aria-label="Business card front">
    <svg class="front-panel" width="600" height="343" viewBox="0 0 600 343" aria-hidden="true">
      <polygon points="271,100 540,0 600,0 600,343 540,343 271,247" fill="var(--lime)"/>
    </svg>
    <div class="brand">
      <span class="brand__square"></span>
      <span class="brand__name">Harbor Constructors</span>
    </div>
    <p class="holder-name">DANIEL MOREAU</p>
    <div class="contact">
      <p class="contact__company">Harbor Constructors Pty Ltd</p>
      <p>PO Box 4180 Lakeside</p>
      <p>LPO Ridgeway WA 6099</p>
      <p class="contact__gap">Registration 48210</p>
      <p>ABN: 52 304 918 276</p>
      <p class="contact__line contact__gap">0400 123 987
        <svg class="contact__icon" viewBox="0 0 12 12" aria-hidden="true"><rect x="3" y="0.5" width="6" height="11" rx="1" fill="none" stroke="var(--ink)" stroke-width="1.2"/><rect x="5" y="9" width="2" height="1" fill="var(--ink)"/></svg>
      </p>
      <p class="contact__line">daniel@harborconstructors.com.au
        <svg class="contact__icon" viewBox="0 0 12 12" aria-hidden="true"><rect x="0.5" y="2.5" width="11" height="7" fill="var(--ink)"/><polyline points="0.5,2.5 6,7 11.5,2.5" fill="none" stroke="var(--lime)" stroke-width="1"/></svg>
      </p>
      <p class="contact__line">www.harborconstructors.com.au
        <svg class="contact__icon" viewBox="0 0 12 12" aria-hidden="true"><circle cx="6" cy="6" r="5.5" fill="var(--ink)"/><ellipse cx="6" cy="6" rx="2.2" ry="5.5" fill="none" stroke="var(--lime)" stroke-width=".8"/><line x1=".5" y1="6" x2="11.5" y2="6" stroke="var(--lime)" stroke-width=".8"/></svg>
      </p>
    </div>
  </section>

  <section class="card card--back" aria-label="Business card back">
    <div class="brand">
      <span class="brand__square"></span>
      <span class="brand__name">Harbor Constructors</span>
    </div>
    <p class="web-band">www.harborconstructors.com.au</p>
  </section>
</body>
</html>
```